Web Design Project

*** This project has been temporarily placed on hold as the Logo Design needs to be completed first. You are all welcome to participate on it as well: http://gigs.pitchboardly.com/brief.aspx?id=482917 This project will be reopened soon***

Revamp current website adding newly designed logo and creating layout that is good on desktops, tablets, and cell phones.

Current website can be viewed at www.vennatistudio.com

Will you see the website is small but graphics heavy in the gallery. The gallery needs to be setup so that it is easy to maintain the links and update the photos.

Needs to have high visual impact.

I need a new logo and website layout designed for my partner's business. This is a birthday present. His business is interior painting, wallpapering and design. He also has access to a wide variety of products including carpet, fabrics, furniture, wallpaper, tile, countertops, etc. I have attached some screen shots of his website for reference. He is a one man shop and has a stellar reputation with his customers. He is on-time, very tidy, excellent with animals, and always finishes on time and on budget. There are no restrictions on colors or fonts. The logo needs to work well with the website, business cards and printed materials. The website needs to flow content for device size so it looks just as good on a cell phone or tablet as it does on a desktop computer. Whatever the heck that's called! Thanks. I am looking forward to seeing everyone's ideas.
Updates

Hi Designers, We've reopened this project as our logo design project has just completed. Please refer to the uploaded files and make use of either Horizontal or Vertical versions of the logo depending on what you think is suitable for your design proposals. We look forward to your creative submissions!

Target Market(s)

Consumers looking for interior design, painting, and wallpapering as well as interior products such as flooring, window treatments, reupholstering, counter tops, etc.

Industry/Entity Type

Cell Phone

Requirements
Must have
• Clean, sharp, visual impact (at least on the home page)
Should not have
• Clutter.

```html
<!DOCTYPE html>
<html lang="en">
<head>
<meta charset="utf-8">
<title>Vennati Interior Designs</title>
<link href="https://fonts.googleapis.com/css2?family=Questrial&family=Crimson+Text&family=Open+Sans:wght@400&display=swap" rel="stylesheet">
<style>
  :root{
    --brand-red:#9a2934;
    --brand-red-light:#b23a45;
    --brand-red-dark:#84232d;
    --footer-red:#8a2a32;
    --accent-orange:#f39200;
    --gallery-title:#d9785a;
    --text-grey:#666666;
    --light-grey:#e2e2e2;
    --white:#ffffff;
  }
  *{margin:0;padding:0;box-sizing:border-box}
  html,body{width:940px;height:1200px;overflow:hidden;background:var(--white)}
  body{position:relative;font-family:"Questrial",sans-serif;color:var(--text-grey)}
  .page{position:relative;width:940px;height:1200px;overflow:hidden}

  .site-header{position:absolute;left:0;top:0;width:940px;height:74px}
  .brand{position:absolute;left:122px;top:24px;font-family:"Questrial",sans-serif;font-size:21px;color:var(--brand-red);letter-spacing:.3px;white-space:nowrap}
  .call{position:absolute;right:117px;top:29px;text-align:right}
  .call-label{font-size:10px;color:#777;display:block}
  .call-number{display:flex;align-items:center;gap:5px;font-size:16px;color:var(--brand-red);margin-top:1px}

  .main-nav{position:absolute;left:0;top:74px;width:940px;height:37px;background:linear-gradient(var(--brand-red-light),var(--brand-red) 55%,var(--brand-red-dark))}
  .main-nav ul{list-style:none;position:absolute;left:157px;top:0;height:37px;display:flex;align-items:center}
  .main-nav li{font-size:12px;color:var(--white);letter-spacing:.2px;display:flex;align-items:center;-webkit-text-stroke:.25px var(--white)}
  .main-nav li+li::before{content:"|";color:rgba(255,255,255,.55);margin:0 20px;font-size:11px;-webkit-text-stroke:0}

  .hero{position:absolute;left:0;top:111px;width:940px;height:362px;
    background:
      radial-gradient(ellipse 260px 120px at 690px 210px,rgba(22,22,22,.92),rgba(22,22,22,0) 100%),
      radial-gradient(ellipse 200px 70px at 720px 150px,rgba(190,190,190,.9),rgba(190,190,190,0) 100%),
      radial-gradient(ellipse 200px 50px at 300px 95px,rgba(150,30,25,.55),rgba(150,30,25,0) 100%),
      radial-gradient(ellipse 420px 90px at 330px 340px,rgba(205,45,25,.95),rgba(205,45,25,0) 100%),
      linear-gradient(180deg,#efeeeb 0%,#e3e1dd 35%,#d9cfc4 55%,#d29a62 72%,#c97a48 88%,#b84a2e 100%)}
  .hero-caption{position:absolute;left:119px;top:131px;width:338px;height:120px;background:rgba(40,40,40,.78);padding:20px 22px}
  .hero-kicker{font-size:17px;color:var(--white)}
  .hero-title{font-size:23px;color:var(--white);margin-top:1px}
  .hero-text{font-family:"Open Sans",sans-serif;font-size:8.5px;line-height:15px;color:#cfcfcf;margin-top:6px}
  .hero-dots{position:absolute;left:447px;top:346px;display:flex;gap:3px}
  .hero-dots span{width:8px;height:8px;border-radius:50%;background:#e8e8e8}

  .welcome{position:absolute;left:0;top:500px;width:940px;text-align:center}
  .welcome h1{font-family:"Crimson Text",serif;font-weight:400;font-size:26px;color:var(--brand-red)}
  .welcome p{font-family:"Open Sans",sans-serif;font-size:8.6px;line-height:17px;color:var(--text-grey);width:606px;margin:5px auto 0}

  .services{position:absolute;left:0;top:609px;width:940px}
  .service{position:absolute;width:180px;text-align:center}
  .service-icon{width:59px;height:59px;border-radius:50%;background:var(--accent-orange);margin:0 auto;display:flex;align-items:center;justify-content:center}
  .service h2{font-weight:400;font-size:14px;color:var(--accent-orange);margin-top:5px}
  .service p{font-family:"Open Sans",sans-serif;font-size:8.6px;line-height:14px;color:#888;margin-top:1px}

  .divider{position:absolute;left:114px;top:748px;width:713px;height:1px;background:var(--light-grey)}

  .gallery-title{position:absolute;left:134px;top:785px;font-family:"Crimson Text",serif;font-weight:400;font-size:19px;color:var(--gallery-title);letter-spacing:.3px}
  .product{position:absolute;width:160px;height:110px;overflow:hidden;box-shadow:0 1px 3px rgba(0,0,0,.25)}
  .product-photo{position:absolute;inset:0}
  .product-bar{position:absolute;left:0;bottom:0;width:100%;height:26px;background:rgba(80,28,32,.82);display:flex;align-items:center;justify-content:space-between;padding:0 8px 0 13px;font-size:12px;color:var(--white)}
  .tone-a{background:radial-gradient(ellipse 30px 60px at 20px 40px,#1e1e1e,rgba(30,30,30,0)),radial-gradient(ellipse 30px 50px at 80px 55px,#f2eee2,rgba(242,238,226,0)),linear-gradient(90deg,#5a4a36 0%,#e3d9bf 40%,#d8cfb3 70%,#efe9da 100%)}
  .tone-b{background:radial-gradient(ellipse 60px 25px at 80px 85px,#3e3e3e,rgba(62,62,62,0)),radial-gradient(ellipse 20px 30px at 75px 35px,#4a2b22,rgba(74,43,34,0)),linear-gradient(180deg,#ebe8e2 0%,#d8d3ca 50%,#8f877c 75%,#6a635a 100%)}
  .tone-c{background:radial-gradient(ellipse 35px 45px at 25px 70px,#b77a3a,rgba(183,122,58,0)),radial-gradient(ellipse 50px 30px at 110px 25px,#f4f2ec,rgba(244,242,236,0)),linear-gradient(180deg,#8f8374 0%,#d6d0c2 40%,#d8d2c3 100%)}
  .tone-d{background:radial-gradient(ellipse 40px 55px at 65px 60px,#4a2418,rgba(74,36,24,0)),radial-gradient(ellipse 30px 30px at 140px 70px,#e8e2d6,rgba(232,226,214,0)),linear-gradient(180deg,#6d2f55 0%,#7c3a62 45%,#3a1f18 100%)}
  .tone-e{background:radial-gradient(ellipse 25px 60px at 20px 60px,#f1efea,rgba(241,239,234,0)),radial-gradient(ellipse 50px 50px at 100px 70px,#8a5a3a,rgba(138,90,58,0)),linear-gradient(90deg,#dedbd3 0%,#c9bfae 50%,#e3dfd4 100%)}
  .tone-f{background:radial-gradient(ellipse 60px 25px at 80px 85px,#1a1a1a,rgba(26,26,26,0)),radial-gradient(ellipse 80px 40px at 80px 25px,#f6f5f1,rgba(246,245,241,0)),linear-gradient(180deg,#efeee9 0%,#d9d5cb 55%,#5b4942 100%)}

  .site-footer{position:absolute;left:0;top:1109px;width:940px;height:91px;background:var(--footer-red)}
  .footer-nav{position:absolute;left:119px;top:28px;list-style:none;display:flex;font-size:11px;color:var(--white)}
  .footer-nav li+li::before{content:"|";margin:0 6px}
  .copyright{position:absolute;left:119px;top:53px;font-family:"Open Sans",sans-serif;font-size:8.6px;color:#e3c3c6}
  .social{position:absolute;left:718px;top:24px;display:flex;gap:2px}
  .social-link{width:21px;height:21px;border-radius:50%;background:var(--white);display:flex;align-items:center;justify-content:center}
</style>
</head>
<body>
<div class="page">
  <header class="site-header">
    <div class="brand">VENNATI INTERIOR DESIGNS</div>
    <div class="call">
      <span class="call-label">Call Us Now</span>
      <span class="call-number">
        <svg width="17" height="17" viewBox="0 0 17 17" aria-hidden="true"><circle cx="8.5" cy="8.5" r="7.7" fill="none" stroke="#999" stroke-width="1"/><path d="M6 4.5l1.6 2-1 1.2a6 6 0 0 0 2.7 2.7l1.2-1 2 1.6-1 1.5c-3.3 0-6.5-3.2-6.5-6.5z" fill="none" stroke="#999" stroke-width="1"/></svg>
        415.555.0172
      </span>
    </div>
  </header>

  <nav class="main-nav">
    <ul>
      <li>HOME</li><li>ABOUT US</li><li>SERVICES</li><li>PRODUCT</li><li>GALLERY</li><li>CONTACT</li>
    </ul>
  </nav>

  <section class="hero" role="img" aria-label="Photo of a modern living room with a black leather sofa, red striped rug and a white kitchen behind">
    <div class="hero-caption">
      <div class="hero-kicker">Morbi porta libero nonummy</div>
      <div class="hero-title">Interior Design &amp; Funiture</div>
      <p class="hero-text">Libero a tempus libero lectus feugiat felis Morbi diam mauris viverra in gravida eu mattis in ante Morbi eget arcu Morbi</p>
    </div>
    <div class="hero-dots"><span></span><span></span><span></span><span></span></div>
  </section>

  <section class="welcome">
    <h1>Welcome to Vennati Interior Designs</h1>
    <p>With the various materials, colors, and finishes available the choices today can be daunting. By listening to you, I am able to pick just the right color, the right fabric, or the right furniture for your projects.Whether you are starting with a small project or a large project, I am ready to bring your ideas to life.<br>It doesn't take a big budget to achieve dramatic effects. A wonderful new look is within anyone's reach.</p>
  </section>

  <section class="services">
    <div class="service" style="left:183px">
      <div class="service-icon">
        <svg width="32" height="32" viewBox="0 0 32 32" aria-hidden="true" fill="none" stroke="#fff" stroke-width="2.4"><rect x="5" y="4" width="20" height="8" rx="1.5"/><path d="M25 8h3v8H15v4"/><rect x="12.5" y="20" width="5" height="9"/></svg>
      </div>
      <h2>Interior painting</h2>
      <p>Etiam est nunc venenatis in tristique eu imperdiet ac nisl Cum sociis nato</p>
    </div>
    <div class="service" style="left:387px">
      <div class="service-icon">
        <svg width="32" height="32" viewBox="0 0 32 32" aria-hidden="true" fill="#fff"><rect x="13" y="13" width="6" height="6" transform="rotate(45 16 16)"/><path d="M16 3l3 5-3 3-3-3zM16 29l3-5-3-3-3 3zM3 16l5-3 3 3-3 3zM29 16l-5-3-3 3 3 3z"/><path d="M6 6h5l-1 4-4 1zM26 6h-5l1 4 4 1zM6 26h5l-1-4-4-1zM26 26h-5l1-4 4-1z"/></svg>
      </div>
      <h2>Wallpapering</h2>
      <p>Etiam est nunc venenatis in tristique eu imperdiet ac nisl Cum sociis</p>
    </div>
    <div class="service" style="left:594px">
      <div class="service-icon">
        <svg width="34" height="34" viewBox="0 0 34 34" aria-hidden="true" fill="none" stroke="#fff" stroke-width="2.2"><rect x="3" y="14" width="28" height="6" transform="rotate(-45 17 17)"/><path d="M6 6l22 22-3 2-21-21z"/><path d="M26 4l4 4"/></svg>
      </div>
      <h2>Design</h2>
      <p>Etiam est nunc venenatis in tristique eu imperdiet ac nisl Cum sociis natoque</p>
    </div>
  </section>

  <div class="divider"></div>

  <h2 class="gallery-title">PRODUCTS GALLERY</h2>

  <article class="product" style="left:135px;top:819px"><div class="product-photo tone-a" role="img" aria-label="Photo of a hallway with patterned wallpaper and a white door"></div><div class="product-bar">Product Name<svg width="8" height="14" viewBox="0 0 8 14" aria-hidden="true"><polyline points="1,1 7,7 1,13" fill="none" stroke="#fff" stroke-width="1.2"/></svg></div></article>
  <article class="product" style="left:306px;top:819px"><div class="product-photo tone-b" role="img" aria-label="Photo of a room with a checkered floor and fireplace"></div><div class="product-bar">Product Name<svg width="8" height="14" viewBox="0 0 8 14" aria-hidden="true"><polyline points="1,1 7,7 1,13" fill="none" stroke="#fff" stroke-width="1.2"/></svg></div></article>
  <article class="product" style="left:476px;top:819px"><div class="product-photo tone-c" role="img" aria-label="Photo of a kitchen with wooden cabinets and tiled floor"></div><div class="product-bar">Product Name<svg width="8" height="14" viewBox="0 0 8 14" aria-hidden="true"><polyline points="1,1 7,7 1,13" fill="none" stroke="#fff" stroke-width="1.2"/></svg></div></article>
  <article class="product" style="left:652px;top:819px"><div class="product-photo tone-c" role="img" aria-label="Photo of a kitchen with wooden cabinets and tiled floor"></div><div class="product-bar">Product Name<svg width="8" height="14" viewBox="0 0 8 14" aria-hidden="true"><polyline points="1,1 7,7 1,13" fill="none" stroke="#fff" stroke-width="1.2"/></svg></div></article>

  <article class="product" style="left:135px;top:939px"><div class="product-photo tone-d" role="img" aria-label="Photo of a dining room with purple walls and a china cabinet"></div><div class="product-bar">Product Name<svg width="8" height="14" viewBox="0 0 8 14" aria-hidden="true"><polyline points="1,1 7,7 1,13" fill="none" stroke="#fff" stroke-width="1.2"/></svg></div></article>
  <article class="product" style="left:306px;top:939px"><div class="product-photo tone-e" role="img" aria-label="Photo of an entry hall with a white staircase"></div><div class="product-bar">Product Name<svg width="8" height="14" viewBox="0 0 8 14" aria-hidden="true"><polyline points="1,1 7,7 1,13" fill="none" stroke="#fff" stroke-width="1.2"/></svg></div></article>
  <article class="product" style="left:476px;top:939px"><div class="product-photo tone-f" role="img" aria-label="Photo of a breakfast nook with white shutters and black chairs"></div><div class="product-bar">Product Name<svg width="8" height="14" viewBox="0 0 8 14" aria-hidden="true"><polyline points="1,1 7,7 1,13" fill="none" stroke="#fff" stroke-width="1.2"/></svg></div></article>
  <article class="product" style="left:652px;top:939px"><div class="product-photo tone-f" role="img" aria-label="Photo of a breakfast nook with white shutters and black chairs"></div><div class="product-bar">Product Name<svg width="8" height="14" viewBox="0 0 8 14" aria-hidden="true"><polyline points="1,1 7,7 1,13" fill="none" stroke="#fff" stroke-width="1.2"/></svg></div></article>

  <footer class="site-footer">
    <ul class="footer-nav">
      <li>HOME</li><li>ABOUT</li><li>SERVICES</li><li>PRODUCT</li><li>GALLERY</li><li>CONTACT</li>
    </ul>
    <p class="copyright">© 2014 Company Name &nbsp;All right reserved &nbsp;Term of Use</p>
    <div class="social" aria-label="Social links">
      <span class="social-link"><svg width="11" height="11" viewBox="0 0 11 11" aria-hidden="true"><circle cx="5.5" cy="5.5" r="3.6" fill="none" stroke="#8a2a32" stroke-width="1.6"/></svg></span>
      <span class="social-link"><svg width="11" height="11" viewBox="0 0 11 11" aria-hidden="true"><circle cx="5.5" cy="5.5" r="3.6" fill="none" stroke="#8a2a32" stroke-width="1.6"/></svg></span>
      <span class="social-link"><svg width="11" height="11" viewBox="0 0 11 11" aria-hidden="true"><circle cx="5.5" cy="5.5" r="3.6" fill="none" stroke="#8a2a32" stroke-width="1.6"/></svg></span>
      <span class="social-link"><svg width="11" height="11" viewBox="0 0 11 11" aria-hidden="true"><circle cx="5.5" cy="5.5" r="3.6" fill="none" stroke="#8a2a32" stroke-width="1.6"/></svg></span>
    </div>
  </footer>
</div>
</body>
</html>
```